Kelvora IT company focused on 3 areas of IT

Looking for something similar to attached cards. Logo for kelvora also attached.. Looking for something clean as far as colors (surprise me).. kelvo stands for 3 primary areas, web design, consulting and network infrastructure design. Please email me if you have any questions. Looking forward to seeing how creative and professional this card will look. Thank you,

Target Market(s)

Small business/consumers looking for It services

Industry/Entity Type

It Service

Contact Information for Business Card

Dorian Vesk
Principal Consultant

202-555-0173

www.kelvora-example.com
dvesk@kelvora-example.com

4172 Marsh Lantern Ct,
Germantown, MD 20000

Colors

Designer to choose colors to be used in the design.

Requirements
Must have
• attached Logo design. Feel free to play with the colors.. If you have a better idea for a card, please fee free to send me. Looking for something clean/modern. Should have tech feel, not cheesy.
Nice to have
• Surprise me :-)..

```html
<!DOCTYPE html>
<html lang="en">
<head>
<meta charset="utf-8">
<title>Kelvora Business Card</title>
<link href="https://fonts.googleapis.com/css2?family=Lato:wght@400;700;900&display=swap" rel="stylesheet">
<style>
  :root {
    --backdrop: #1b1c1c;
    --card: #1c2b2b;
    --ink: #ffffff;
    --ink-soft: #e6ecec;
  }
  html, body {
    margin: 0;
    padding: 0;
    width: 1200px;
    height: 900px;
    overflow: hidden;
    background: var(--backdrop);
    font-family: "Lato", sans-serif;
  }
  .canvas {
    position: relative;
    width: 1200px;
    height: 900px;
  }
  .card {
    position: absolute;
    width: 520px;
    height: 300px;
    background: var(--card);
    border-radius: 16px;
    box-shadow: 0 14px 30px rgba(0,0,0,0.45);
    color: var(--ink);
  }
  .card--front { left: 110px; top: 110px; }
  .card--back  { left: 570px; top: 470px; }

  .brand {
    position: absolute;
    display: flex;
    align-items: center;
    gap: 12px;
  }
  .brand__mark {
    width: 22px;
    height: 22px;
    background: var(--ink);
  }
  .brand__name {
    font-weight: 900;
    font-size: 40px;
    letter-spacing: 1px;
    color: var(--ink);
  }
  .card--front .brand { left: 50%; top: 96px; transform: translateX(-50%); }
  .card--back .brand  { left: 40px; top: 206px; }
  .card--back .brand__name { font-size: 34px; }
  .card--back .brand__mark { width: 18px; height: 18px; }

  .website {
    position: absolute;
    left: 0; right: 0;
    top: 208px;
    text-align: center;
    font-weight: 700;
    font-size: 13px;
    letter-spacing: 3.5px;
    color: var(--ink);
  }

  .person {
    position: absolute;
    right: 34px;
    top: 34px;
    text-align: right;
  }
  .person__name {
    font-size: 15px;
    font-weight: 400;
    color: var(--ink-soft);
  }
  .person__name strong { font-weight: 700; color: var(--ink); }
  .person__title {
    font-size: 11px;
    margin-top: 3px;
    color: var(--ink-soft);
  }

  .contact {
    position: absolute;
    right: 24px;
    top: 158px;
    list-style: none;
    margin: 0;
    padding: 0;
    font-size: 12px;
    line-height: 1.55;
    color: var(--ink-soft);
    text-align: right;
  }
  .contact li {
    display: flex;
    justify-content: flex-end;
    align-items: flex-start;
    gap: 8px;
  }
  .contact__icon {
    width: 12px;
    height: 12px;
    margin-top: 3px;
    flex: none;
  }
  .contact__icon--blank { visibility: hidden; }
</style>
</head>
<body>
<div class="canvas">

  <section class="card card--front">
    <div class="brand">
      <span class="brand__mark"></span>
      <span class="brand__name">Kelvora</span>
    </div>
    <div class="website">www.kelvora-example.com</div>
  </section>

  <section class="card card--back">
    <div class="person">
      <div class="person__name">Dorian <strong>Vesk</strong></div>
      <div class="person__title">Chief Executive Offer</div>
    </div>

    <ul class="contact">
      <li>202-555-0173
        <svg class="contact__icon" viewBox="0 0 12 12" aria-hidden="true">
          <path d="M1 4.5 Q6 1 11 4.5 L10 6 L8 5.2 L8 4 Q6 3.4 4 4 L4 5.2 L2 6 Z M3 7 H9 L10 11 H2 Z" fill="#fff"/>
        </svg>
      </li>
      <li>dvesk@kelvora-example.com
        <svg class="contact__icon" viewBox="0 0 12 12" aria-hidden="true">
          <rect x="0.5" y="2.5" width="11" height="7.5" fill="#fff"/>
          <path d="M0.5 2.5 L6 7 L11.5 2.5" fill="none" stroke="#1c2b2b" stroke-width="1"/>
        </svg>
      </li>
      <li>4172 Marsh Lantern Ct,
        <svg class="contact__icon" viewBox="0 0 12 12" aria-hidden="true">
          <path d="M6 11.5 C3 8 2 6.5 2 4.5 A4 4 0 0 1 10 4.5 C10 6.5 9 8 6 11.5 Z" fill="#fff"/>
          <circle cx="6" cy="4.5" r="1.5" fill="#1c2b2b"/>
        </svg>
      </li>
      <li>Germantown, MD 20000
        <svg class="contact__icon contact__icon--blank" viewBox="0 0 12 12" aria-hidden="true"></svg>
      </li>
    </ul>

    <div class="brand">
      <span class="brand__mark"></span>
      <span class="brand__name">Kelvora</span>
    </div>
  </section>

</div>
</body>
</html>
```